Menu Design Project

Hi! I am looking for a menu design for a company opening up in Downtown Dallas. The company's name is Marbury Bakes and the colors are Tiffany Blue and Brown. The company is a cupcake factory and the vibe we are going for is a cupcake/coffee shop where people can come in, relax and still be able to work on work stuff etc. Think wood, glass and stainless steel. Very modern and professional. We would love for the menu to be kept simple, not too complicated and perhaps try to keep it at 1 double sided sheet of paper. The ones we have currently at a store are 4X6, but 5X7 sounds good too.
Updates

Hi!

We would like to have two different size options, 4X6 and 5X7. We want a menu that is portable, that customers can take with them and that we can include in their carry-out bags. We want it to be double sided to maximize the space. I have also uploaded an example of what we are looking for, feel free to use those names in your menu and prices, we might change them afterwards.Thanks,

Industry/Entity Type

Store

Requirements
Must have
• Must be Tiffany Blue and Brown. Must have the store's logo on there (attached), map for location, information about facebook page, and mobile app. We are going to have about 27 different cupcake flavors but we will also be making cakepops, cakes and beverages (lattes, cappuccinos, frappes, smoothies, coffee, hot cocoa, etc).

Store Address: 2917 Quill Ave, Dallas TX 75431

Store Hours:
Mon-Thur 10am-9pm
Fri-Sat 10am-10pm
Sun 12pm-7pm

Phone number: 2145831097

website: www.marburybakes-demo.com
Nice to have
• Would love for it to be double sided.

```html
<!DOCTYPE html>
<html lang="en">
<head>
<meta charset="utf-8">
<title>Marbury Bakes – Menu &amp; Pricing</title>
<link href="https://fonts.googleapis.com/css2?family=Open+Sans:ital,wght@0,300;0,400;0,600;0,700;1,600&display=swap" rel="stylesheet">
<style>
  :root {
    --tiffany: #55b6c6;
    --brown: #2e1a1c;
    --taupe: #978c8b;
    --white: #ffffff;
    --map-light: #e4e4e4;
    --map-dark: #c9c9c9;
  }
  * { box-sizing: border-box; margin: 0; padding: 0; }
  html, body { width: 857px; height: 1200px; overflow: hidden; background: var(--white); }
  body { font-family: "Open Sans", Arial, sans-serif; }
  .menu-sheet { position: relative; width: 857px; height: 1200px; background: var(--white); overflow: hidden; }

  .top-band { position: absolute; left: 0; top: 0; width: 100%; height: 30px; background: var(--tiffany); }

  .brand { position: absolute; left: 0; top: 30px; width: 100%; height: 197px;
    display: flex; align-items: center; justify-content: center; gap: 16px; }
  .brand-dot { width: 22px; height: 22px; border-radius: 50%; background: var(--tiffany); }
  .brand-name { font-size: 62px; font-weight: 300; color: var(--tiffany); letter-spacing: 1px; }

  .section-band { position: absolute; left: 0; width: 100%; background: var(--tiffany); }
  .band-menu { top: 227px; height: 34px; }
  .band-menu h2 { position: absolute; left: 31px; top: 0; font-size: 27px; font-weight: 400; line-height: 34px; color: var(--brown); }
  .band-enjoy { top: 704px; height: 37px; }
  .band-enjoy h2 { text-align: center; font-size: 27px; font-weight: 400; line-height: 37px; color: var(--white); }

  .drinks { position: absolute; left: 0; top: 261px; width: 100%; height: 443px; background: var(--taupe); color: var(--white); }
  .drinks-tab { position: absolute; left: 29px; top: 10px; width: 428px; height: 26px; background: var(--brown);
    font-size: 20px; line-height: 26px; padding-left: 2px; }
  .drink-col { position: absolute; list-style: none; font-size: 21px; line-height: 29px; }
  .drink-col.hot { left: 30px; top: 38px; width: 356px; }
  .drink-col.cold { left: 461px; top: 41px; width: 356px; }
  .col-title { display: block; }
  .item { display: flex; white-space: nowrap; }
  .leader { flex: 1; overflow: hidden; }
  .leader::after { content: "...................................................................................."; }

  .corporate-box { position: absolute; left: 509px; top: 296px; width: 292px; height: 110px;
    border: 5px solid var(--brown); border-radius: 22px; display: flex; flex-direction: column;
    align-items: center; justify-content: center; font-weight: 700; font-size: 19px; line-height: 29px; text-align: center; }
  .corporate-box .spaced { letter-spacing: 6px; }

  .location { position: absolute; left: 45px; top: 751px; width: 305px; color: var(--brown); }
  .location-lead { font-size: 18px; font-weight: 700; line-height: 30px; text-align: justify; text-align-last: left; }
  .location-lead .wide { letter-spacing: 5px; }
  .directions { margin-top: 14px; font-size: 16px; line-height: 23.5px; text-align: justify; letter-spacing: 0.6px; }

  .map-frame { position: absolute; left: 427px; top: 757px; width: 369px; height: 251px; background: var(--tiffany); }
  .map-corner { position: absolute; width: 80px; height: 70px; background: var(--brown); }
  .map-corner.tr { right: 0; top: 0; }
  .map-corner.bl { left: 0; bottom: 0; }
  .map-area { position: absolute; left: 0; top: 12px; width: 357px; height: 239px;
    background: linear-gradient(135deg, var(--map-light), var(--map-dark)); }

  .footer { position: absolute; left: 0; top: 1044px; width: 100%; height: 156px; background: var(--tiffany); }
  .contact-box { position: absolute; left: 113px; top: 16px; width: 327px; height: 127px;
    border: 5px solid var(--brown); border-radius: 22px; color: var(--white);
    font-size: 18px; font-weight: 700; line-height: 26px; text-align: center;
    display: flex; flex-direction: column; justify-content: center; }
  .hours-box { position: absolute; left: 444px; top: 16px; width: 299px; height: 124px;
    border: 4px solid var(--white); border-radius: 22px; color: var(--brown);
    font-size: 18px; font-weight: 600; font-style: italic; line-height: 26px; padding-top: 8px; }
  .hours-box h3 { font-size: 18px; font-weight: 600; text-align: center; }
  .hours-row { display: flex; padding-left: 30px; }
  .hours-row .day { width: 125px; }
</style>
</head>
<body>
<main class="menu-sheet">
  <div class="top-band"></div>

  <header class="brand">
    <span class="brand-dot"></span>
    <h1 class="brand-name">Marbury Bakes</h1>
  </header>

  <div class="section-band band-menu"><h2>menu &amp; pricing</h2></div>

  <section class="drinks">
    <div class="drinks-tab">to drink</div>
    <ul class="drink-col hot">
      <li class="col-title">hot beverages</li>
      <li class="item">coffee<span class="leader"></span> $2.00</li>
      <li class="item">expresso shot<span class="leader"></span> $2.00</li>
      <li class="item">cafe latte<span class="leader"></span> $2.00</li>
      <li class="item">vainilla latte<span class="leader"></span> $2.00</li>
      <li class="item">caramel macchiato<span class="leader"></span> $2.00</li>
      <li class="item">caffe mocha<span class="leader"></span> $2.00</li>
      <li class="item">capuccino<span class="leader"></span> $2.00</li>
      <li class="item">americano<span class="leader"></span> $2.00</li>
      <li class="item">chai tea latte<span class="leader"></span> $2.00</li>
      <li class="item">tea<span class="leader"></span> $2.00</li>
      <li class="item">hot chocolate<span class="leader"></span> $2.00</li>
    </ul>
    <ul class="drink-col cold">
      <li class="col-title">cold beverages</li>
      <li class="item">frozen caramel latte<span class="leader"></span> $2.00</li>
      <li class="item">frozen mocha<span class="leader"></span> $2.00</li>
      <li class="item">very berry smoothie<span class="leader"></span> $2.00</li>
      <li class="item">strawberry banana smoothie<span class="leader"></span> $2.00</li>
      <li class="item">sweet tea<span class="leader"></span> $2.00</li>
      <li class="item">bottled water<span class="leader"></span> $2.00</li>
      <li class="item">bottled drinks<span class="leader"></span> $2.00</li>
    </ul>
    <div class="corporate-box">
      <span class="spaced">Ask us about</span>
      <span class="spaced">our corporate</span>
      <span>prices and special!"</span>
    </div>
  </section>

  <div class="section-band band-enjoy"><h2>come &amp; enjoy!</h2></div>

  <section class="location">
    <p class="location-lead">Marbury Bakes is located in <span class="wide">Downtown Dallas,</span> where Quill Ave meets N Harlow St.</p>
    <p class="directions">If you are traveling North East on Redfield Freeway, take the exit to ward Tanner St and merge onto N Tanner St. Turn left onto Calder St. and take the 2nd right onto N Harlow St. Take a right onto Quill Ave, will be on the left.</p>
  </section>

  <div class="map-frame">
    <div class="map-corner tr"></div>
    <div class="map-corner bl"></div>
    <div class="map-area" role="img" aria-label="Street map of downtown Dallas marking the shop at Quill Ave and N Harlow St"></div>
  </div>

  <footer class="footer">
    <address class="contact-box">
      <span>2917 Quill Ave, Dallas TX 75431</span>
      <span>2145831097</span>
      <span>www.marburybakes-demo.com</span>
      <span>info@marburybakes-demo.com</span>
    </address>
    <div class="hours-box">
      <h3>Store Hours</h3>
      <div class="hours-row"><span class="day">Mon-Thur</span><span>10am-9pm</span></div>
      <div class="hours-row"><span class="day">Fri-Sat</span><span>10am-10pm</span></div>
      <div class="hours-row"><span class="day">Sun</span><span>12pm-7pm</span></div>
    </div>
  </footer>
</main>
</body>
</html>
```